TALRENO Business Cards

We require a business card for our company that provides IT consulting services. We already have a logo that needs to be used on the card. We want a clean professional looking design that incorporates our colours. Our main focus is providing managed services to business, which involves us looking after all of their IT requirements including managing servers/networks, projects, and procurement.

Industry/Entity Type

Information Technology

Requirements
Must have
• our logo, contact information, name, title, phone numbers

```html
<!DOCTYPE html>
<html lang="en">
<head>
<meta charset="UTF-8">
<title>TALRENO Business Cards</title>
<link rel="stylesheet" href="https://fonts.googleapis.com/css2?family=Work+Sans:wght@400;500;600&display=swap">
<style>
  :root {
    --backdrop: #2a2a2c;
    --card: #161616;
    --card-edge: #222224;
    --brand-blue: #1b95d6;
    --text-light: #eeeeee;
    --text-muted: #cfcfcf;
    --logo-silver: #bdbdbd;
  }
  * { margin: 0; padding: 0; box-sizing: border-box; }
  html, body {
    width: 1200px; height: 900px; overflow: hidden;
    background: var(--backdrop);
    font-family: "Work Sans", Arial, sans-serif;
  }
  .canvas {
    width: 1200px; height: 900px;
    display: flex; flex-direction: column; align-items: center; justify-content: center;
    gap: 48px;
  }
  .card {
    width: 660px; height: 378px;
    background: var(--card);
    border: 1px solid var(--card-edge);
    position: relative;
    box-shadow: 0 18px 40px rgba(0,0,0,0.45);
  }
  /* Back side */
  .card-back .wordmark {
    position: absolute; left: 0; right: 0; top: 140px;
    text-align: center;
    font-size: 58px; font-weight: 600; letter-spacing: 4px;
    color: var(--logo-silver);
  }
  .card-back .site {
    position: absolute; left: 0; right: 0; bottom: 28px;
    text-align: center; font-size: 15px; color: var(--text-light);
  }
  .accent { color: var(--brand-blue); }
  /* Front side */
  .card-front .wordmark {
    position: absolute; left: 60px; top: 160px;
    font-size: 50px; font-weight: 600; letter-spacing: 3px;
    color: var(--brand-blue);
  }
  .card-front .divider {
    position: absolute; left: 368px; top: 78px;
    width: 2px; height: 216px;
    background: linear-gradient(to bottom, transparent, var(--brand-blue) 20%, var(--brand-blue) 80%, transparent);
  }
  .details {
    position: absolute; left: 398px; top: 78px; right: 24px;
    color: var(--text-light);
  }
  .details .name {
    font-size: 22px; font-weight: 500; letter-spacing: 2px;
    color: var(--brand-blue); text-transform: uppercase;
  }
  .details .title { font-size: 16px; color: var(--text-muted); margin-bottom: 18px; }
  .details .address { font-size: 16px; line-height: 1.45; margin-bottom: 14px; }
  .contact-list { list-style: none; font-size: 16px; line-height: 1.6; }
  .contact-list li { display: flex; align-items: center; gap: 10px; }
  .contact-list svg { width: 13px; height: 13px; flex: none; }
</style>
</head>
<body>
<main class="canvas">
  <section class="card card-back">
    <div class="wordmark">TALRENO</div>
    <div class="site">www.<span class="accent">talreno</span>.com</div>
  </section>

  <section class="card card-front">
    <div class="wordmark">TALRENO</div>
    <div class="divider"></div>
    <div class="details">
      <div class="name">Dana Whitfield</div>
      <div class="title">Director</div>
      <div class="address">48 Birch Avenue<br>Box 2710, Red Deer, AB</div>
      <ul class="contact-list">
        <li>
          <svg viewBox="0 0 16 16" aria-hidden="true"><path d="M4 1l2.5 3-1.5 2c1 2 3 4 5 5l2-1.5 3 2.5-1.5 2.5C7 16 0 9 1.5 2.5z" fill="var(--brand-blue)"/></svg>
          403-555-0182
        </li>
        <li>
          <svg viewBox="0 0 16 16" aria-hidden="true"><rect x="1" y="3" width="14" height="10" fill="none" stroke="var(--brand-blue)" stroke-width="1.5"/><path d="M1 3l7 6 7-6" fill="none" stroke="var(--brand-blue)" stroke-width="1.5"/></svg>
          info@talreno.com
        </li>
        <li>
          <svg viewBox="0 0 16 16" aria-hidden="true"><circle cx="8" cy="8" r="6.5" fill="none" stroke="var(--brand-blue)" stroke-width="1.4"/><ellipse cx="8" cy="8" rx="3" ry="6.5" fill="none" stroke="var(--brand-blue)" stroke-width="1.2"/><path d="M1.5 8h13" stroke="var(--brand-blue)" stroke-width="1.2"/></svg>
          <span>www.<span class="accent">talreno</span>.com</span>
        </li>
      </ul>
    </div>
  </section>
</main>
</body>
</html>
```